Business Card for Coach - ready to print

Design Business Card ready to order prints www.lukasbrenner.coach

* An Overview / Background of the Business & Services
· Coaching
· Personal growth
* The Target Market / Audience you are trying to reach
· private person in different roles (self, familiy, business role)s
* Design Specifics; any preferences or ideas for Style, Colour, Imagery, etc
· See www.lukasbrenner.coach
· "simple" design
· (small) element of surprise / unusual element

* Information that will be placed in the Business Card
· Beratung und Coaching
· Address: Lukas Brenner, Talmatt 42, CH-8531 Winterthur, Mobile +41 76 254 63 07
* Do you have an existing website or Facebook page where designers can learn more about your company?
· lukasbrenner.coach

Target Market(s)

private person in different roles (self, familiy, business role)

Industry/Entity Type

Life Coaching

Contact Information for Business Card

Lukas Brenner
Talmatt 42
CH-8531 Winterthur

Mobile: +41 76 254 63 07
Email: lubr@sonnwelt.ch
www.lukasbrenner.coach

Font styles to use
Sans Serif

Colors

Designer to choose colors to be used in the design.

Requirements
Must have
• "simple" design
• element of surprise / unusual element
• Beratung & Coaching
• see www.lukasbrenner.coach for colors and so...
Nice to have
• TA Symbol (three rings on top of each other) - unsual presentation
• QR Code of Website (see if it fits in and still looks good).

```html
<!DOCTYPE html>
<html lang="de">
<head>
<meta charset="utf-8">
<title>Lukas Brenner – Business Card</title>
<link rel="stylesheet" href="https://fonts.googleapis.com/css2?family=Heebo:wght@400;500;600&display=swap">
<style>
  :root {
    --bg: #9a9a9a;
    --brand-blue: #0b8cbd;
    --brand-blue-light: #1a9bcb;
    --line-blue: #3fb4e6;
    --paper: #ffffff;
    --ink-grey: #6a6a6a;
    --white: #ffffff;
  }
  * { margin: 0; padding: 0; box-sizing: border-box; }
  html, body {
    width: 1200px;
    height: 930px;
    overflow: hidden;
    background: var(--bg);
    font-family: "Heebo", "Helvetica Neue", Arial, sans-serif;
  }
  .stage {
    position: relative;
    width: 1200px;
    height: 930px;
  }
  .card {
    position: absolute;
    left: 300px;
    width: 600px;
    height: 388px;
    border-radius: 28px;
    box-shadow: 0 6px 18px rgba(0,0,0,0.25);
    overflow: hidden;
  }
  .card--front {
    top: 56px;
    background: linear-gradient(100deg, var(--brand-blue-light) 0%, var(--brand-blue) 100%);
    display: flex;
    flex-direction: column;
    align-items: center;
    justify-content: center;
    color: var(--white);
    text-transform: uppercase;
    font-weight: 500;
    font-size: 13px;
    letter-spacing: 0.04em;
    line-height: 1.75;
    text-align: center;
  }
  .card--back {
    top: 486px;
    background: var(--paper);
  }
  .identity {
    position: absolute;
    left: 40px;
    top: 238px;
  }
  .identity__name {
    color: var(--brand-blue);
    font-size: 26px;
    font-weight: 500;
    letter-spacing: 0.01em;
    text-transform: uppercase;
    line-height: 1;
  }
  .identity__role {
    color: var(--ink-grey);
    font-size: 16px;
    margin-top: 2px;
    margin-left: 16px;
  }
  .divider {
    position: absolute;
    left: 56px;
    right: 40px;
    top: 296px;
    height: 1px;
    background: var(--line-blue);
  }
  .contact {
    position: absolute;
    left: 56px;
    top: 310px;
    color: var(--ink-grey);
    font-size: 13.5px;
    line-height: 1.75;
    letter-spacing: 0.01em;
    white-space: nowrap;
  }
  .contact__row:nth-child(2) { padding-left: 18px; }
</style>
</head>
<body>
<main class="stage">
  <section class="card card--front">
    <p class="tagline">Coaching / Personal Growth</p>
    <p class="tagline">The Target Market / Audience You Are Trying To Reach</p>
  </section>

  <section class="card card--back">
    <div class="identity">
      <h1 class="identity__name">Lukas Brenner</h1>
      <p class="identity__role">Coach</p>
    </div>
    <div class="divider"></div>
    <address class="contact" style="font-style: normal;">
      <p class="contact__row">P : +41 76 254 63 07 | E : lubr@sonnwelt.ch | W : www.lukasbrenner.coach</p>
      <p class="contact__row">A : Talmatt 42 CH-8531 Winterthur</p>
    </address>
  </section>
</main>
</body>
</html>
```